Residential Roofing Company, need a Unique business card for a Woman owned ompany

Woman Owned Residential Roofing Company. Specializing in Insurance Claims
Attention to Detail is what sets this woman owned roofing company apart from the rest
We are TRV Certified and are an Accredited business with an A rating with the QPL. Our Contractor License number KMT48395

```html
<!DOCTYPE html>
<html lang="en">
<head>
<meta charset="utf-8">
<title>Crestline Roofing – Business Card</title>
<link rel="stylesheet" href="https://fonts.googleapis.com/css2?family=Montserrat:wght@400;500;700;800&display=swap">
<style>
  :root {
    --page: #e9eaec;
    --navy: #0b2f63;
    --navy-deep: #082552;
    --brand-blue: #2a86e6;
    --ink: #0a0a0a;
    --paper: #ffffff;
    --badge-red: #d8262b;
    --badge-grey: #8a8d92;
    --text-light: #ffffff;
  }
  * { box-sizing: border-box; margin: 0; padding: 0; }
  html, body { width: 1200px; height: 874px; overflow: hidden; }
  body {
    background: var(--page);
    font-family: "Montserrat", sans-serif;
    position: relative;
  }
  .card {
    position: absolute;
    left: 270px;
    width: 660px;
    height: 377px;
    overflow: hidden;
    box-shadow: 0 6px 18px rgba(0,0,0,.18);
  }
  /* Front */
  .card-front { top: 30px; background: var(--navy); }
  .front-wordmark {
    position: absolute; left: 0; right: 0; top: 120px;
    text-align: center;
    font-weight: 800; font-size: 40px; letter-spacing: 1px;
    color: var(--brand-blue);
  }
  .front-mark-dot {
    display: inline-block; width: 16px; height: 16px;
    background: var(--brand-blue); margin-right: 14px; vertical-align: 4px;
  }
  .tagline {
    position: absolute; left: 170px; right: 170px; top: 222px;
    border-top: 1px solid rgba(255,255,255,.7);
    border-bottom: 1px solid rgba(255,255,255,.7);
    padding: 8px 0;
    text-align: center; color: var(--text-light); font-size: 19px;
  }
  .tagline strong { font-weight: 700; }
  .tagline span { font-weight: 400; }
  .badge-certified {
    position: absolute; left: 34px; bottom: 40px;
    width: 124px; height: 40px;
    background: linear-gradient(90deg, var(--badge-red) 0 26%, var(--badge-red) 26%, #e23a3a 100%);
    border-top: 6px solid var(--badge-grey);
  }
  .badge-accredited {
    position: absolute; right: 34px; bottom: 36px;
    width: 112px; height: 46px;
    background: var(--paper); border-radius: 5px;
    border-left: 30px solid #1b3f78;
  }
  /* Back */
  .card-back { top: 437px; background: var(--paper); display: flex; }
  .contact-panel {
    width: 265px; height: 100%;
    background: var(--ink); color: var(--text-light);
    padding: 62px 0 0 34px;
  }
  .person-name { font-weight: 700; font-size: 21px; letter-spacing: .5px; }
  .person-role { font-size: 14px; margin-bottom: 20px; }
  .address { font-size: 13.5px; line-height: 1.35; margin-bottom: 8px; }
  .contact-list { list-style: none; font-size: 13.5px; line-height: 1.5; }
  .contact-list li { display: flex; align-items: center; gap: 8px; }
  .contact-list svg { width: 12px; height: 12px; fill: var(--text-light); flex: none; }
  .license { font-size: 13.5px; margin-top: 8px; }
  .brand-panel { position: relative; flex: 1; }
  .back-wordmark {
    position: absolute; left: 0; right: 0; top: 108px;
    text-align: center;
    font-weight: 800; font-size: 32px; color: var(--navy);
  }
  .roofline-art {
    position: absolute; left: 0; right: 0; bottom: 0; height: 150px;
    background: linear-gradient(180deg, var(--paper) 0%, var(--navy) 55%, var(--navy-deep) 100%);
  }
</style>
</head>
<body>
  <section class="card card-front" aria-label="Card front">
    <div class="front-wordmark"><span class="front-mark-dot"></span>CRESTLINE ROOFING</div>
    <p class="tagline"><strong>woman owned</strong> <span>roofing company</span></p>
    <div class="badge-certified" role="img" aria-label="TRV certified contractor badge"></div>
    <div class="badge-accredited" role="img" aria-label="QPL accredited business badge"></div>
  </section>

  <section class="card card-back" aria-label="Card back">
    <div class="contact-panel">
      <h1 class="person-name">DANIEL REEVE</h1>
      <p class="person-role">President</p>
      <p class="address">4120 Willow Bend Road<br>Juneau, Alaska 99801</p>
      <ul class="contact-list">
        <li><svg viewBox="0 0 24 24"><path d="M6.6 10.8a15 15 0 006.6 6.6l2.2-2.2c.3-.3.7-.4 1-.2 1.1.4 2.3.6 3.6.6.6 0 1 .4 1 1V20c0 .6-.4 1-1 1A17 17 0 013 4c0-.6.4-1 1-1h3.5c.6 0 1 .4 1 1 0 1.3.2 2.5.6 3.6.1.3 0 .7-.2 1z"/></svg>555-214-0386</li>
        <li><svg viewBox="0 0 24 24"><path d="M7 1h10a2 2 0 012 2v18a2 2 0 01-2 2H7a2 2 0 01-2-2V3a2 2 0 012-2zm0 3v14h10V4z"/></svg>555-318-7742</li>
        <li><svg viewBox="0 0 24 24"><path d="M2 5h20v14H2zm2 2v.5l8 5 8-5V7z"/></svg>info@crestlineroofing.com</li>
        <li><svg viewBox="0 0 24 24"><circle cx="12" cy="12" r="10"/></svg>www.crestlineroofing.com</li>
      </ul>
      <p class="license">Lic No KMT48395</p>
    </div>
    <div class="brand-panel">
      <div class="back-wordmark">CRESTLINE ROOFING</div>
      <div class="roofline-art" role="img" aria-label="Brand roofline artwork in navy"></div>
    </div>
  </section>
</body>
</html>
```